Professional Trustee Company - Business Cards
Thornwick Crest Fiduciary Services, Inc.
Designers:
(1) Please be sure that the logo is large enough to be easily read as in some cases it appears like the words are too small to read.
(2) Please have the back of the card read: Earning your trust is our business.
RT/KPH/WN Team
Please note that I am also looking for stationary and envelope designs in black and white only. Thank you!

```html
<!DOCTYPE html>
<html lang="en">
<head>
<meta charset="utf-8">
<title>Thornwick Crest Fiduciary Services – Business Card</title>
<link href="https://fonts.googleapis.com/css2?family=Cinzel:wght@400;600&family=Cormorant+SC:wght@400;500&display=swap" rel="stylesheet">
<style>
  :root {
    --page-bg: #e9e7e4;
    --card-bg: #ffffff;
    --ink-dark: #3c3c3c;
    --ink-mid: #5a5a5a;
    --ink-soft: #8a8a8a;
    --icon-bg: #4a4a4a;
    --icon-fg: #ffffff;
  }
  html, body {
    margin: 0;
    padding: 0;
    width: 1200px;
    height: 914px;
    overflow: hidden;
    background: var(--page-bg);
  }
  .canvas {
    width: 1200px;
    height: 914px;
    display: flex;
    align-items: center;
    justify-content: center;
  }
  .business-card {
    position: relative;
    width: 1000px;
    height: 572px;
    background: var(--card-bg);
    box-shadow: 0 2px 10px rgba(0,0,0,0.12);
    color: var(--ink-mid);
    font-family: "Cormorant SC", Georgia, serif;
  }
  .brand {
    position: absolute;
    left: 0;
    right: 0;
    top: 150px;
    display: flex;
    align-items: center;
    justify-content: center;
    gap: 26px;
  }
  .brand-mark {
    width: 96px;
    height: 96px;
    border-radius: 50%;
    background: var(--ink-dark);
    flex: none;
  }
  .brand-text {
    font-family: "Cinzel", Georgia, serif;
    font-weight: 600;
    color: var(--ink-dark);
    line-height: 1;
  }
  .brand-name {
    font-size: 58px;
    letter-spacing: 6px;
  }
  .brand-sub {
    margin-top: 8px;
    font-size: 23px;
    letter-spacing: 2px;
  }
  .tagline {
    margin-top: 8px;
    font-family: "Cinzel", Georgia, serif;
    font-size: 10px;
    letter-spacing: 3px;
    color: var(--ink-soft);
  }
  .holder {
    position: absolute;
    left: 0;
    right: 0;
    top: 318px;
    text-align: center;
    font-size: 21px;
    letter-spacing: 1px;
    color: var(--ink-mid);
  }
  .contact-list {
    position: absolute;
    left: 60px;
    right: 60px;
    display: flex;
    gap: 46px;
    font-size: 18px;
    letter-spacing: 0.5px;
    color: var(--ink-mid);
  }
  .contact-list.row-one { top: 424px; }
  .contact-list.row-two { top: 470px; }
  .contact-item {
    display: flex;
    align-items: center;
    gap: 10px;
    white-space: nowrap;
  }
  .contact-icon {
    width: 20px;
    height: 20px;
    flex: none;
  }
</style>
</head>
<body>
<main class="canvas">
  <section class="business-card" aria-label="Business card front">
    <div class="brand">
      <span class="brand-mark"></span>
      <div class="brand-text">
        <div class="brand-name">THORNWICK CREST</div>
        <div class="brand-sub">FIDUCIARY SERVICES</div>
        <div class="tagline">EARNING YOUR TRUST IS OUR BUSINESS</div>
      </div>
    </div>

    <p class="holder">Daniel Reese Marlowe, JD, TEP &nbsp;|&nbsp; President &amp; Founder</p>

    <div class="contact-list row-one">
      <span class="contact-item">
        <svg class="contact-icon" viewBox="0 0 20 20"><circle cx="10" cy="10" r="10" fill="var(--icon-bg)"/><path d="M7 5.5l1.6 0.4 0.6 2.3-1.1 0.9a6 6 0 0 0 2.8 2.8l0.9-1.1 2.3 0.6 0.4 1.6c-0.4 1-1.4 1.5-2.4 1.3A8 8 0 0 1 5.7 7.9C5.5 6.9 6 5.9 7 5.5z" fill="var(--icon-fg)"/></svg>
        206.555.0147
      </span>
      <span class="contact-item">
        <svg class="contact-icon" viewBox="0 0 20 20"><circle cx="10" cy="10" r="10" fill="var(--icon-bg)"/><rect x="6" y="5" width="8" height="4" fill="var(--icon-fg)"/><rect x="5" y="9" width="10" height="4" rx="1" fill="var(--icon-fg)"/><rect x="7" y="12" width="6" height="3" fill="var(--icon-fg)"/></svg>
        206.555.0182
      </span>
      <span class="contact-item">
        <svg class="contact-icon" viewBox="0 0 20 20"><circle cx="10" cy="10" r="10" fill="var(--icon-bg)"/><rect x="5" y="6.5" width="10" height="7" fill="var(--icon-fg)"/><path d="M5 6.5l5 4 5-4" fill="none" stroke="var(--icon-bg)" stroke-width="1"/></svg>
        daniel@thornwickcrest.com
      </span>
    </div>

    <div class="contact-list row-two">
      <span class="contact-item">
        <svg class="contact-icon" viewBox="0 0 20 20"><circle cx="10" cy="10" r="10" fill="var(--icon-bg)"/><path d="M10 4.5a3.5 3.5 0 0 1 3.5 3.5c0 2.6-3.5 7-3.5 7s-3.5-4.4-3.5-7A3.5 3.5 0 0 1 10 4.5z" fill="var(--icon-fg)"/><circle cx="10" cy="8" r="1.3" fill="var(--icon-bg)"/></svg>
        1420 Harbor Ridge Lane NE Cedar Point, WA 98000
      </span>
      <span class="contact-item">
        <svg class="contact-icon" viewBox="0 0 20 20"><circle cx="10" cy="10" r="10" fill="var(--icon-bg)"/><circle cx="10" cy="10" r="5" fill="none" stroke="var(--icon-fg)" stroke-width="1.2"/><ellipse cx="10" cy="10" rx="2.2" ry="5" fill="none" stroke="var(--icon-fg)" stroke-width="1"/><line x1="5" y1="10" x2="15" y2="10" stroke="var(--icon-fg)" stroke-width="1"/></svg>
        www.thornwickcrest.com
      </span>
    </div>
  </section>
</main>
</body>
</html>
```